Newly established winery needs label for its bottles

The Corvelle-Marsan Winery, is a small family owned winery that has been producing wine for little over 3 years. We are now ready to officially start commercializing our products. To do so we are looking for a label for our wine bottles. We are looking for a creative design that will differentiate our bottles from the more conventional labels. We are looking for one label design with 3 color schemes so that we can have a standard look and feel for all three of our wines, while having some differentiation between them with the different color schemes. In summary we are looking for a label that will standout by its uniqueness, simplicity and its modern touch. The label should also reflect the historical significance of the name of the winery. The attached documents offers more detail about the winery, what we are looking for, as well as some technical specification for the label. This label project is also related to a logo project see brief: http://www.pitchgallery.example/project-progress.aspx?briefId=553184). The logo project is now complete and the winning design source files were added to the documents in this brief. Also, details around the information that will need to appear on the label was added to the document list.
Updates
This label project will be on hold temporarily while the logo project is in progress. If you are interested in participating in the logo project, please follow this link: http://www.pitchgallery.example/project-progress.aspx?briefId=553184 Added Wednesday, December 17, 2014
Reason: Deadline extended to give sufficent time for submission and modification to the designs provided.

```html
<!DOCTYPE html>
<html lang="en">
<head>
<meta charset="utf-8">
<title>Corvelle-Marsan Winery – White Wine Label</title>
<link rel="stylesheet" href="https://fonts.googleapis.com/css2?family=Cinzel:wght@600;700&family=IM+Fell+English+SC&family=Montserrat:wght@700&display=swap">
<style>
  :root {
    --backdrop: #2a2522;
    --paper-light: #c07438;
    --paper-mid: #a2592a;
    --paper-dark: #6e3516;
    --paper-edge: #4a230e;
    --stain: #7a3a16;
    --ink-emboss: #5e2e12;
    --ink-highlight: rgba(235, 165, 105, 0.4);
    --spine-gold: #c9a23a;
    --ink-print: #1e0f06;
  }
  * { margin: 0; padding: 0; box-sizing: border-box; }
  html, body {
    width: 1072px;
    height: 1200px;
    overflow: hidden;
    background: var(--backdrop);
  }
  .label {
    position: absolute;
    left: 146px;
    top: 50px;
    width: 780px;
    height: 1100px;
  }
  .label__paper {
    position: absolute;
    inset: 0;
    width: 780px;
    height: 1100px;
  }
  .embossed {
    color: var(--ink-emboss);
    text-shadow: 1px 1px 0 var(--ink-highlight), -1px -1px 0 rgba(40, 15, 4, 0.25);
  }

  /* Crest area */
  .crest {
    position: absolute;
    left: 60px;
    top: 110px;
    width: 650px;
    height: 400px;
  }
  .crest__ring {
    position: absolute;
    left: 205px;
    top: 20px;
    width: 240px;
    height: 240px;
    border: 7px solid var(--ink-emboss);
    border-radius: 50%;
    box-shadow: 1px 1px 0 var(--ink-highlight), inset 1px 1px 0 var(--ink-highlight);
  }
  .crest__rule {
    position: absolute;
    height: 3px;
    background: var(--ink-emboss);
    box-shadow: 1px 1px 0 var(--ink-highlight);
  }
  .crest__rule--left  { left: 10px;  width: 200px; }
  .crest__rule--right { left: 440px; width: 200px; }
  .crest__rule--top    { top: 100px; }
  .crest__rule--bottom { top: 188px; }
  .crest__tag {
    position: absolute;
    top: 114px;
    width: 190px;
    font-family: "Cinzel", serif;
    font-weight: 600;
    font-size: 22px;
    line-height: 30px;
    letter-spacing: 4px;
  }
  .crest__tag--left  { left: 14px;  text-align: left; }
  .crest__tag--right { left: 446px; text-align: right; }
  .crest__name {
    position: absolute;
    left: 0;
    top: 300px;
    width: 650px;
    text-align: center;
    font-family: "Cinzel", serif;
    font-weight: 700;
    font-size: 54px;
    letter-spacing: 5px;
  }

  .vintage {
    position: absolute;
    left: 148px;
    top: 728px;
    font-family: "Cinzel", serif;
    font-weight: 600;
    font-size: 52px;
    letter-spacing: 4px;
  }
  .varietal {
    position: absolute;
    left: 30px;
    top: 800px;
    font-family: "IM Fell English SC", serif;
    font-weight: 400;
    font-size: 84px;
    letter-spacing: 0;
  }
  .varietal__flourish {
    position: absolute;
    left: 360px;
    top: 800px;
    width: 330px;
    height: 190px;
  }

  .legal {
    position: absolute;
    top: 1064px;
    font-family: "Montserrat", sans-serif;
    font-weight: 700;
    font-size: 22px;
    letter-spacing: 1px;
    color: var(--ink-print);
  }
  .legal--volume { left: 18px; }
  .legal--alcohol { right: 26px; }
</style>
</head>
<body>
  <main class="label">
    <svg class="label__paper" viewBox="0 0 780 1100" role="img" aria-label="Aged orange-brown paper texture with a torn right edge and a gilded spine line">
      <defs>
        <radialGradient id="paperTone" cx="0.42" cy="0.42" r="0.75">
          <stop offset="0" stop-color="var(--paper-light)"/>
          <stop offset="0.6" stop-color="var(--paper-mid)"/>
          <stop offset="1" stop-color="var(--paper-dark)"/>
        </radialGradient>
        <linearGradient id="tornShade" x1="0" x2="1">
          <stop offset="0.82" stop-color="var(--paper-edge)" stop-opacity="0"/>
          <stop offset="1" stop-color="var(--paper-edge)" stop-opacity="0.85"/>
        </linearGradient>
        <radialGradient id="stain">
          <stop offset="0" stop-color="var(--stain)" stop-opacity="0.45"/>
          <stop offset="1" stop-color="var(--stain)" stop-opacity="0"/>
        </radialGradient>
        <radialGradient id="glow">
          <stop offset="0" stop-color="#d4894a" stop-opacity="0.4"/>
          <stop offset="1" stop-color="#d4894a" stop-opacity="0"/>
        </radialGradient>
        <clipPath id="paperShape">
          <path d="M0 0 H730 L748 40 L742 90 L768 150 L756 210 L772 280 L758 350 L746 420 L762 500 L740 560 L736 640 L756 700 L748 760 L766 830 L750 900 L756 960 L744 1020 L752 1070 L748 1100 H0 Z"/>
        </clipPath>
      </defs>
      <g clip-path="url(#paperShape)">
        <rect width="780" height="1100" fill="url(#paperTone)"/>
        <ellipse cx="180" cy="560" rx="200" ry="140" fill="url(#stain)"/>
        <ellipse cx="560" cy="620" rx="180" ry="120" fill="url(#stain)"/>
        <ellipse cx="420" cy="480" rx="220" ry="120" fill="url(#glow)"/>
        <ellipse cx="300" cy="960" rx="260" ry="120" fill="url(#stain)"/>
        <ellipse cx="640" cy="150" rx="160" ry="120" fill="url(#stain)"/>
        <ellipse cx="120" cy="120" rx="160" ry="110" fill="url(#glow)"/>
        <path d="M690 0 L780 0 L780 120 Q730 60 690 0 Z" fill="var(--paper-edge)" opacity="0.55"/>
        <rect width="780" height="1100" fill="url(#tornShade)"/>
        <rect x="0" y="0" width="14" height="1100" fill="var(--paper-edge)" opacity="0.6"/>
        <line x1="20" y1="0" x2="20" y2="1100" stroke="var(--spine-gold)" stroke-width="3" opacity="0.75"/>
        <line x1="30" y1="0" x2="30" y2="1100" stroke="var(--paper-edge)" stroke-width="2" opacity="0.5"/>
      </g>
    </svg>

    <header class="crest embossed">
      <span class="crest__ring" aria-hidden="true"></span>
      <span class="crest__rule crest__rule--left crest__rule--top" aria-hidden="true"></span>
      <span class="crest__rule crest__rule--left crest__rule--bottom" aria-hidden="true"></span>
      <span class="crest__rule crest__rule--right crest__rule--top" aria-hidden="true"></span>
      <span class="crest__rule crest__rule--right crest__rule--bottom" aria-hidden="true"></span>
      <p class="crest__tag crest__tag--left">VIGNOBLE<br>FAMILIAL</p>
      <p class="crest__tag crest__tag--right">FAMILY<br>WINERY</p>
      <div class="crest__name">CORVELLE-MARSAN</div>
    </header>

    <p class="vintage embossed">2014</p>
    <h1 class="varietal embossed">WHiTE WiNE</h1>
    <svg class="varietal__flourish" viewBox="0 0 330 190" role="img" aria-label="Embossed calligraphic flourish">
      <defs>
        <radialGradient id="flourishTone">
          <stop offset="0" stop-color="var(--ink-emboss)" stop-opacity="0.5"/>
          <stop offset="1" stop-color="var(--ink-emboss)" stop-opacity="0"/>
        </radialGradient>
      </defs>
      <ellipse cx="165" cy="100" rx="165" ry="80" fill="url(#flourishTone)"/>
    </svg>

    <p class="legal legal--volume">750 ML.</p>
    <p class="legal legal--alcohol">ALC. 12% BY VOLUME</p>
  </main>
</body>
</html>
```